Innovative and exciting banner advert for real estate
Lots of freedom of design
#10 I like the way the 'save thousands in commission' is done with mixed size font. The 'save thousands' stands out very clearly which is important to us
Thanks.
Hi and thank you designers for your attention to our project, there are some great ideas coming in now.
A slight change to the brief:
In the blue screen, please remove 'money back guarantee' and replace with 'no hidden charges' from the green screen so each screen has only 3 bullet points.
Thanks
RPellow
Hi Designers
Please note, we do not require the logo in the adverts just the use of the logo colours as the base.
It is more important that the first line of text stands out. If you are going to insert the logo, please make it a minor element or as #4 has cleverly used it for the bullet points.
Thanks designers for your time and great ideas. #4 I like the way you have used the logo symbol in the bullet points, and that you have aligned the bullets points to the left, it looks good.
#5 the way that 'save thousands' and 'get the best price' stand out clearly is great, this is the message that we are trying to pass on to viewers, it is most important.
If there is any information you need please contact me directly, I will check messages.
Just to clarify, we do not require the logo in the adverts just the use of the logo colours as the base. These adverts are going to be used on our own site.
Regards
Thanks Hostmod for making that clear for designers.
Designers, we don't have images of the product we sell as we provide real estate services (not goods). If looking for inspiration for imagery, residential property is more appropriate than commercial property.
Thanks everyone.
Attention Designers!
PH is looking for static banner design which includes two individual advert frames.
Banner size : 450 wide x 225 high
I'm clarifying with our site technicians exactly what the frames should be.
We originally wanted two individual advert frames, 450 wide x 225 high, with no animation in the frames themselves. However, when trying to work within the Tandelvox fields, we couldn't elect the specific size we required and instead had to opt for a package deal.
I will upload a link to the real estate website template we will be using, the template has 'featured property' images in the centre of the homepage which we will be replacing with our two adverts. That is, we will not have the featured property on the home page at all.
http://skins.brovellanstudio.example/?theme=realestate2
Dear PH,
Is this animated gifs or flash?

```html
<!DOCTYPE html>
<html lang="en">
<head>
<meta charset="utf-8">
<title>Save Thousands in Commission – Banner</title>
<link rel="stylesheet" href="https://fonts.googleapis.com/css2?family=Roboto+Condensed:wght@700&display=swap">
<style>
  :root {
    --navy-deep: #0a2a66;
    --navy: #0e3a82;
    --band-top: #2a74d2;
    --band-bottom: #1654ae;
    --band-edge: #5d9ae6;
    --bevel: #0b3274;
    --square-light: #6fb0f2;
    --square-dark: #2a6fc8;
    --white: #ffffff;
  }
  html, body {
    margin: 0;
    padding: 0;
    width: 1200px;
    height: 600px;
    overflow: hidden;
    background: var(--navy-deep);
  }
  .banner {
    position: relative;
    width: 1200px;
    height: 600px;
    overflow: hidden;
    background: linear-gradient(180deg, var(--navy) 0%, var(--navy-deep) 100%);
    font-family: "Roboto Condensed", "Arial Narrow", sans-serif;
    font-weight: 700;
    color: var(--white);
  }
  .banner-frame {
    position: absolute;
    inset: 0;
  }
  .headline {
    position: absolute;
    top: 62px;
    left: 92px;
    display: flex;
    align-items: center;
  }
  .headline-mark {
    width: 116px;
    height: 116px;
    border-radius: 6px;
    background: linear-gradient(135deg, var(--square-light), var(--square-dark));
    box-shadow: inset 0 0 0 3px rgba(255,255,255,0.35);
  }
  .headline-save {
    margin-left: 22px;
    font-size: 152px;
    line-height: 1;
    letter-spacing: -2px;
    text-shadow: 0 3px 4px rgba(0,0,0,0.35);
  }
  .headline-detail {
    margin-left: 34px;
    display: flex;
    flex-direction: column;
    align-items: center;
    line-height: 0.92;
    text-shadow: 0 2px 3px rgba(0,0,0,0.35);
  }
  .headline-thousands { font-size: 82px; letter-spacing: 1px; }
  .headline-commission { font-size: 72px; }
  .benefits {
    position: absolute;
    top: 280px;
    left: 98px;
    margin: 0;
    padding: 0;
    list-style: none;
  }
  .benefit {
    display: flex;
    align-items: center;
    height: 86px;
    font-size: 52px;
    letter-spacing: 0.5px;
    text-shadow: 0 2px 3px rgba(0,0,0,0.35);
  }
  .benefit-marker {
    flex: none;
    width: 42px;
    height: 42px;
    margin-right: 26px;
    border-radius: 3px;
    background: linear-gradient(135deg, var(--square-light), var(--square-dark));
    box-shadow: inset 0 0 0 2px rgba(255,255,255,0.35);
  }
</style>
</head>
<body>
  <div class="banner">
    <svg class="banner-frame" width="1200" height="600" viewBox="0 0 1200 600" aria-hidden="true">
      <defs>
        <linearGradient id="band-fill" x1="0" y1="0" x2="0" y2="1">
          <stop offset="0" stop-color="var(--band-top)"/>
          <stop offset="1" stop-color="var(--band-bottom)"/>
        </linearGradient>
      </defs>
      <polygon points="0,0 1200,0 1200,255 0,255" fill="url(#band-fill)"/>
      <polygon points="0,0 40,0 40,215 0,255" fill="var(--bevel)"/>
      <polygon points="1200,0 1160,0 1160,215 1200,255" fill="var(--bevel)"/>
      <polygon points="40,0 1160,0 1160,20 40,20" fill="var(--bevel)" opacity="0.55"/>
      <line x1="40" y1="215" x2="1160" y2="215" stroke="var(--band-edge)" stroke-width="2" opacity="0.6"/>
      <line x1="0" y1="255" x2="1200" y2="255" stroke="var(--band-edge)" stroke-width="3"/>
    </svg>

    <div class="headline">
      <div class="headline-mark" aria-hidden="true"></div>
      <span class="headline-save">SAVE</span>
      <div class="headline-detail">
        <span class="headline-thousands">THOUSANDS</span>
        <span class="headline-commission">IN COMMISSION</span>
      </div>
    </div>

    <ul class="benefits">
      <li class="benefit"><span class="benefit-marker" aria-hidden="true"></span>PRIVATE PROPERTY SALES SOLUTIONS</li>
      <li class="benefit"><span class="benefit-marker" aria-hidden="true"></span>ASSISTED PROPERTY SALES EXPERTISE</li>
      <li class="benefit"><span class="benefit-marker" aria-hidden="true"></span>NO HIDDEN CHARGES</li>
    </ul>
  </div>
</body>
</html>
```